Brenwick Realty
Business cards and stationery
Brenwick Realty - Real Estate
Creative Brief
Modern
Marian Talcott
Director
Level 4 218 Garnet Lane Melbourne VIC 3000
marian@brenwickrealty-example.com.au
www.brenwickrealty-example.com.au
Brenwick Summit Realty 518902K Licensee Marian Talcott
Stationery needs to have the licensee info on the bottom of letterhead
black background logo in centre

```html
<!DOCTYPE html>
<html lang="en">
<head>
<meta charset="utf-8">
<title>Brenwick Realty – Stationery Concepts</title>
<link rel="stylesheet" href="https://fonts.googleapis.com/css2?family=Montserrat:wght@400;700&display=swap">
<style>
:root{
  --pink:#d4147e;
  --blue:#1ea2dc;
  --ink:#111114;
  --paper:#ffffff;
  --grey-text:#6d6d72;
  --label:#d9d9d9;
  --bg-centre:#cfcfd1;
  --bg-edge:#4b4b4e;
}
*{box-sizing:border-box;margin:0;padding:0}
html,body{width:1200px;height:386px;overflow:hidden}
body{font-family:"Montserrat",sans-serif;background:radial-gradient(ellipse at 50% 45%,var(--bg-centre) 0%,#a9a9ac 45%,var(--bg-edge) 100%);position:relative}
.wordmark{font-weight:700;color:var(--pink);letter-spacing:-0.5px;line-height:1;white-space:nowrap}
.wordmark.on-dark{color:var(--paper)}
.brand-title{position:absolute;left:34px;top:70px;width:240px;text-align:center}
.brand-title .wordmark{font-size:46px}
.brand-title .dot{display:inline-block;width:12px;height:12px;border-radius:50%;background:var(--pink);margin-left:4px}
.brand-title .subtitle{margin-top:52px;font-size:13px;color:#f2f2f2}
.card{position:absolute;width:118px;height:64px;overflow:hidden;box-shadow:0 2px 4px rgba(0,0,0,.4)}
.card.black{background:var(--ink)}
.card.blue{background:var(--blue)}
.card .wave{position:absolute;left:0;bottom:0;width:100%;height:24px}
.card .wordmark{position:absolute;left:0;right:0;top:18px;text-align:center;font-size:15px}
.card .contact{position:absolute;left:8px;top:8px;font-size:4.5px;line-height:1.5;color:#eee;white-space:nowrap}
.card .contact strong{display:block;font-size:6px;color:var(--pink)}
.label{position:absolute;font-size:5px;color:var(--label);white-space:nowrap}
.letterhead{position:absolute;top:20px;width:148px;height:332px;background:var(--paper);box-shadow:0 2px 6px rgba(0,0,0,.35);overflow:hidden}
.letterhead .head-wave{position:absolute;left:0;top:0;width:148px;height:46px}
.letterhead .foot-wave{position:absolute;left:0;bottom:0;width:148px;height:22px}
.letterhead .wordmark{position:absolute;left:9px;top:12px;font-size:9px}
.letterhead .contact{position:absolute;right:6px;top:9px;font-size:3.3px;line-height:1.5;color:var(--grey-text);text-align:right;white-space:nowrap}
.letterhead.dark-head .contact{color:#cfcfd1}
.letterhead .licensee{position:absolute;left:0;right:0;bottom:24px;text-align:center;font-size:3.4px;color:var(--grey-text);line-height:1.5}
.envelope{position:absolute;left:870px;width:222px;height:84px;box-shadow:0 2px 5px rgba(0,0,0,.4);overflow:hidden}
.envelope svg{position:absolute;inset:0;width:100%;height:100%}
.envelope .wordmark{position:absolute;left:0;right:0;top:11px;text-align:center;font-size:14px}
.envelope.black{background:var(--ink);top:26px}
.envelope.pink{background:var(--pink);top:66px}
.envelope.blue{background:var(--blue);top:106px}
.envelope.white{background:var(--paper);top:146px}
</style>
</head>
<body>

<section class="brand-title">
  <span class="wordmark">brenwick</span><span class="dot"></span>
  <p class="subtitle">Stationery Concepts</p>
</section>

<div class="card black" style="left:16px;top:232px">
  <span class="wordmark">brenwick</span>
  <svg class="wave" viewBox="0 0 118 24" preserveAspectRatio="none"><path d="M0 18 C30 6 70 22 118 10" fill="none" stroke="var(--pink)" stroke-width="2"/><path d="M0 22 C40 12 80 24 118 16" fill="none" stroke="#fff" stroke-width="0.7"/></svg>
</div>
<p class="label" style="left:16px;top:298px">Card Front A</p>
<div class="card black" style="left:146px;top:232px">
  <p class="contact"><strong>Marian Talcott</strong>Director<br>Level 4 218 Garnet Lane Melbourne VIC 3000<br>marian@brenwickrealty-example.com.au<br>www.brenwickrealty-example.com.au</p>
  <svg class="wave" viewBox="0 0 118 24" preserveAspectRatio="none"><path d="M0 18 C30 6 70 22 118 10" fill="none" stroke="var(--pink)" stroke-width="2"/></svg>
</div>
<p class="label" style="left:146px;top:298px">Card Back A</p>
<div class="card blue" style="left:16px;top:310px">
  <span class="wordmark on-dark">brenwick</span>
  <svg class="wave" viewBox="0 0 118 24" preserveAspectRatio="none"><path d="M0 18 C30 6 70 22 118 10" fill="none" stroke="#fff" stroke-width="2"/></svg>
</div>
<p class="label" style="left:16px;top:376px">Card Front B</p>
<div class="card black" style="left:146px;top:310px">
  <p class="contact"><strong>Marian Talcott</strong>Director<br>Level 4 218 Garnet Lane Melbourne VIC 3000<br>marian@brenwickrealty-example.com.au<br>www.brenwickrealty-example.com.au</p>
  <svg class="wave" viewBox="0 0 118 24" preserveAspectRatio="none"><path d="M0 18 C30 6 70 22 118 10" fill="none" stroke="var(--blue)" stroke-width="2"/></svg>
</div>
<p class="label" style="left:146px;top:376px">Card Back B</p>

<article class="letterhead" style="left:312px">
  <svg class="head-wave" viewBox="0 0 148 46" preserveAspectRatio="none"><path d="M0 0 H58 C48 14 28 28 0 34 Z" fill="var(--ink)"/><path d="M0 34 C28 28 50 14 62 0 H68 C54 20 32 36 0 41 Z" fill="var(--pink)"/></svg>
  <span class="wordmark on-dark">brenwick</span>
  <p class="contact">Marian Talcott – Director<br>Level 4 218 Garnet Lane Melbourne VIC 3000<br>marian@brenwickrealty-example.com.au<br>www.brenwickrealty-example.com.au</p>
  <p class="licensee">Brenwick Summit Realty 518902K<br>Licensee Marian Talcott</p>
  <svg class="foot-wave" viewBox="0 0 148 22" preserveAspectRatio="none"><path d="M0 14 C50 4 100 20 148 8" fill="none" stroke="var(--pink)" stroke-width="1.2" opacity=".5"/></svg>
</article>
<p class="label" style="left:352px;top:358px">Letterhead Concept A</p>

<article class="letterhead dark-head" style="left:480px">
  <svg class="head-wave" viewBox="0 0 148 46" preserveAspectRatio="none"><path d="M0 0 H148 V33 C100 38 50 30 0 38 Z" fill="var(--ink)"/><path d="M0 38 C50 30 100 38 148 33 V37 C100 42 50 34 0 43 Z" fill="var(--pink)"/></svg>
  <span class="wordmark on-dark">brenwick</span>
  <p class="contact">Marian Talcott – Director<br>Level 4 218 Garnet Lane Melbourne VIC 3000<br>marian@brenwickrealty-example.com.au<br>www.brenwickrealty-example.com.au</p>
  <p class="licensee">Brenwick Summit Realty 518902K<br>Licensee Marian Talcott</p>
  <svg class="foot-wave" viewBox="0 0 148 22" preserveAspectRatio="none"><path d="M0 14 C50 4 100 20 148 8" fill="none" stroke="var(--pink)" stroke-width="1.2" opacity=".5"/></svg>
</article>
<p class="label" style="left:520px;top:358px">Letterhead Concept B</p>

<div class="envelope black">
  <svg viewBox="0 0 222 84" preserveAspectRatio="none"><path d="M0 0 L111 46 L222 0" fill="none" stroke="#333" stroke-width="1"/></svg>
  <span class="wordmark on-dark">brenwick</span>
</div>
<div class="envelope pink">
  <svg viewBox="0 0 222 84" preserveAspectRatio="none"><path d="M0 0 L111 46 L222 0" fill="none" stroke="#b00f68" stroke-width="1"/></svg>
  <span class="wordmark on-dark">brenwick</span>
</div>
<div class="envelope blue">
  <svg viewBox="0 0 222 84" preserveAspectRatio="none"><path d="M0 0 L111 46 L222 0" fill="none" stroke="#1784b4" stroke-width="1"/></svg>
  <span class="wordmark on-dark">brenwick</span>
</div>
<div class="envelope white">
  <svg viewBox="0 0 222 84" preserveAspectRatio="none"><path d="M0 0 L111 46 L222 0" fill="none" stroke="#ddd" stroke-width="1"/><path d="M0 78 C70 66 150 84 222 70" fill="none" stroke="var(--pink)" stroke-width="1.5"/></svg>
  <span class="wordmark">brenwick</span>
</div>
<p class="label" style="left:956px;top:236px">Envelope Concepts</p>

</body>
</html>
```